Brantwell Group needs a business card design

We need a new business card design using the logo recently selected in a logo competition on Pixel Forum. Our business is a consultancy specializing in aviation and energy and the winning business card design will promote an image of precision and professionalism with creativity.

Please use the logo with the name on the front of the card and use a complementary font. Make the back white with either the light grey or dark grey logo.

Target Market(s)

Senior finance and legal leaders at aviation and energy companies

Industry/Entity Type

Management Consulting

Contact Information for Business Card

Peter Haldane
President
Brantwell Group

www.brantwellgroup.example

(555) 304-6198
ph@brantwellgroup.example

Requirements
Must have
• Professional font that goes well with the logo font

```html
<!DOCTYPE html>
<html lang="en">
<head>
<meta charset="utf-8">
<title>Brantwell Group – Business Card</title>
<link rel="stylesheet" href="https://fonts.googleapis.com/css2?family=Arimo:wght@400&display=swap">
<style>
  :root {
    --backdrop: #2a2a2c;
    --card: #f7f7f7;
    --navy: #1b3f70;
    --ink: #4a4a4a;
    --deco-front: rgba(214, 216, 224, 0.55);
    --deco-back: rgba(196, 199, 212, 0.85);
    --font-text: "Arimo", Arial, Helvetica, sans-serif;
  }
  * { margin: 0; padding: 0; box-sizing: border-box; }
  html, body {
    width: 1200px;
    height: 1001px;
    overflow: hidden;
    background: var(--backdrop);
    font-family: var(--font-text);
  }
  .stage {
    position: relative;
    width: 1200px;
    height: 1001px;
  }
  .card {
    position: absolute;
    left: 306px;
    width: 588px;
    height: 330px;
    background: var(--card);
    box-shadow: 0 6px 14px rgba(0, 0, 0, 0.45);
    overflow: hidden;
  }
  .card--front { top: 123px; }
  .card--back { top: 548px; }

  .decoration {
    position: absolute;
    right: 0;
    bottom: 0;
  }
  .card--front .decoration {
    width: 350px;
    height: 250px;
    background: linear-gradient(135deg, rgba(247,247,247,0) 35%, var(--deco-front) 75%);
  }
  .card--back .decoration {
    width: 480px;
    height: 330px;
    background: linear-gradient(135deg, rgba(247,247,247,0) 30%, var(--deco-back) 80%);
  }

  .brand {
    position: absolute;
    left: 40px;
    top: 0;
    width: 192px;
    height: 170px;
    text-align: center;
    color: var(--navy);
    font-weight: 400;
    z-index: 1;
  }
  .brand__mark {
    position: absolute;
    left: 85px;
    top: 54px;
    width: 22px;
    height: 22px;
    background: var(--navy);
  }
  .brand__name {
    position: absolute;
    left: -10px;
    right: -10px;
    top: 114px;
    font-size: 29px;
    letter-spacing: 1px;
    line-height: 32px;
  }
  .brand__sub {
    position: absolute;
    left: 0;
    right: 0;
    top: 148px;
    font-size: 12px;
    letter-spacing: 17px;
    padding-left: 17px;
    line-height: 14px;
    color: var(--ink);
  }

  .contact {
    position: absolute;
    left: 40px;
    top: 199px;
    width: 192px;
    text-align: center;
    color: var(--ink);
    z-index: 1;
  }
  .contact__name {
    color: var(--navy);
    font-size: 19px;
    line-height: 22px;
  }
  .contact__title {
    font-size: 13px;
    line-height: 16px;
    margin-bottom: 13px;
  }
  .contact__line {
    font-size: 13px;
    line-height: 16px;
    white-space: nowrap;
  }
</style>
</head>
<body>
<main class="stage">
  <section class="card card--front" aria-label="Card front">
    <div class="decoration" role="img" aria-label="Faint brand decoration in the lower right corner"></div>
    <div class="brand">
      <span class="brand__mark" aria-hidden="true"></span>
      <span class="brand__name">BRANTWELL</span>
      <span class="brand__sub">GROUP</span>
    </div>
    <div class="contact">
      <p class="contact__name">PETER HALDANE</p>
      <p class="contact__title">President</p>
      <p class="contact__line">(555) 304-6198</p>
      <p class="contact__line">ph@brantwellgroup.example</p>
      <p class="contact__line">www.brantwellgroup.example</p>
    </div>
  </section>

  <section class="card card--back" aria-label="Card back">
    <div class="decoration" role="img" aria-label="Large light grey brand decoration across the right side"></div>
    <div class="brand">
      <span class="brand__mark" aria-hidden="true"></span>
      <span class="brand__name">BRANTWELL</span>
      <span class="brand__sub">GROUP</span>
    </div>
  </section>
</main>
</body>
</html>
```